UK Glass Restoration Company needs a Direct Mail Postcard Design

We need a HARD HITTING, COMPELLING 300dpi Camera Ready double sided postcard.
The dimensions will be 109mm x 152mm including bleed. We are a scratched glass repair / etched graffiti removal glass restoration company based in London, UK.
We operate mainly within the construction and commercial marketplace, however this particular postcard design is aimed solely at shop owners who have become victims of vandalism, due to etched graffiti tags and or scratches being left on their shop front glass.
We wish to focus the shop / business owners mind to the negative impact such vandalism has on the image of their business and how we are able to offer a quick and cost effective solution
We will supply text for both sides of the postcard along with relevant images, company logo and previous flyer designs, however we are happy for the selected designer to source suitable alternative images provided they are in keeping with the exact "Before" and "After" theme.
The finished postcard must preferably have a white background, but again we are open to creative suggestions.
Target Market(s)
UK SHOP OWNERS
Industry/Entity Type
It Company

```html
<!DOCTYPE html>
<html lang="en">
<head>
<meta charset="utf-8">
<title>Lucent Glass Repairs – Postcard</title>
<link href="https://fonts.googleapis.com/css2?family=Arimo:ital,wght@1,700&family=Source+Sans+3:ital,wght@0,300;0,400;0,600;1,400&display=swap" rel="stylesheet">
<style>
  :root {
    --red: #ec2a30;
    --grey-band: #e2e2e2;
    --photo-panel: #f1eff1;
    --paper: #ffffff;
    --ink: #1c1c1c;
    --body-ink: #333333;
    --brand-blue: #1a8fd6;
    --rule: #e6e6e6;
  }
  * { margin: 0; padding: 0; box-sizing: border-box; }
  html, body { width: 960px; height: 1200px; overflow: hidden; background: var(--paper); }
  .postcard {
    position: relative; width: 960px; height: 1200px; background: var(--paper);
    font-family: "Source Sans 3", "Myriad Pro", sans-serif; color: var(--body-ink);
  }
  .top-bar { position: absolute; left: 20px; top: 0; width: 920px; height: 41px; background: var(--red); }
  .headline-band {
    position: absolute; left: 20px; top: 47px; width: 920px; height: 226px; background: var(--grey-band);
    display: flex; align-items: center; justify-content: center;
  }
  .headline {
    font-family: "Arimo", Arial, sans-serif; font-style: italic; font-weight: 700;
    color: var(--red); font-size: 64px; line-height: 82px; text-align: center; letter-spacing: 0.5px;
  }
  .photo-panel { position: absolute; left: 20px; top: 285px; width: 920px; height: 415px; background: var(--photo-panel); }
  .photo-before {
    position: absolute; left: 152px; top: 0; width: 616px; height: 415px;
    background: radial-gradient(ellipse at 55% 45%, #d9a154 0%, #b97a2c 45%, #6e4413 100%);
  }
  .caption-bar {
    position: absolute; left: 20px; top: 700px; width: 920px; height: 32px; background: var(--red);
    color: #fff; font-style: italic; font-weight: 400; font-size: 25px; line-height: 32px; text-align: center; letter-spacing: 0.5px;
  }
  .intro { position: absolute; left: 49px; top: 742px; width: 870px; }
  .intro-heading { font-style: italic; font-weight: 400; font-size: 30px; color: var(--ink); line-height: 40px; }
  .intro-body { font-weight: 300; font-size: 24.5px; line-height: 34.5px; color: var(--body-ink); margin-top: 2px; letter-spacing: 0.2px; }
  .coupon-note { position: absolute; left: 0; top: 960px; width: 960px; text-align: center; color: var(--red); font-size: 26px; font-weight: 400; }
  .call-line { position: absolute; left: 0; top: 995px; width: 960px; text-align: center; color: var(--ink); font-size: 26px; }
  .call-line .phone { color: var(--red); font-weight: 600; font-size: 34px; }
  .divider { position: absolute; left: 30px; top: 1049px; width: 900px; height: 2px; background: linear-gradient(90deg, transparent, var(--rule) 15%, var(--rule) 85%, transparent); }
  .brand-name { position: absolute; left: 49px; top: 1085px; color: var(--brand-blue); font-size: 44px; font-weight: 400; letter-spacing: 0.5px; }
  .contact { position: absolute; right: 48px; top: 1108px; text-align: right; font-size: 22px; line-height: 30px; }
  .contact-web { color: var(--ink); }
  .contact-phone { color: #555; }
  .contact svg { vertical-align: -2px; margin-right: 6px; }
</style>
</head>
<body>
<main class="postcard">
  <div class="top-bar"></div>
  <header class="headline-band">
    <h1 class="headline">Don't let vandals wreck<br>your image!</h1>
  </header>
  <section class="photo-panel">
    <div class="photo-before" role="img" aria-label="Shop window with estate agent property displays behind glass scratched by etched graffiti"></div>
  </section>
  <div class="caption-bar">Before repair – a bad first impression.</div>
  <section class="intro">
    <h2 class="intro-heading">What's on display in your shop window?</h2>
    <p class="intro-body">If it's graffiti, vandalism, or just wear and tear,&nbsp; that's the first impression your customers get – and it's not good.&nbsp; Lucent Glass Repairs remove damage from glass windows, making them sparkling clear – without replacing the glass! Our glass repair work is effective, green, and very economical.</p>
  </section>
  <p class="coupon-note">See our coupon on the other side to save even more!</p>
  <p class="call-line">Call now for expert advice : <span class="phone">0800 555 0148</span></p>
  <div class="divider"></div>
  <footer>
    <div class="brand-name">Lucent Glass Repairs</div>
    <div class="contact">
      <div class="contact-web"><svg width="18" height="18" viewBox="0 0 18 18" fill="none" stroke="#333" stroke-width="1.4"><circle cx="9" cy="9" r="7.5"/><ellipse cx="9" cy="9" rx="3.2" ry="7.5"/><line x1="1.5" y1="9" x2="16.5" y2="9"/><line x1="3" y1="5" x2="15" y2="5"/><line x1="3" y1="13" x2="15" y2="13"/></svg>www.lucentglassrepairs.co.uk</div>
      <div class="contact-phone"><svg width="16" height="16" viewBox="0 0 16 16"><path fill="#555" d="M3.2 1.5l2.3 2.6-1.2 1.6c.9 1.9 2.3 3.3 4.2 4.2l1.6-1.2 2.6 2.3-1.4 2.2C6.4 13 3 9.6 1.2 3.2z"/></svg>0800 555 0148</div>
    </div>
  </footer>
</main>
</body>
</html>
```